Soy Candle Business needs a label design

We need a label design for a new company selling soy candles - Velvet Hearth Studio.

We are using apothecary jars in 3 sizes.
As per attached candles will be dressed with a beautiful black bow and all finished with a diamante in centre of bow.

We would like label done on lid of candle jars - 5cm circle (5cm from one side to the other), this way one label will fit each product size. Label will be done as a sticker.

We are thinking of the background colour to be black, however are open to recommendations. We want label to be classy, elegant and simple.

Inspiration for candle design came from attached invitation that features the bow, and beautiful vintage paper on top area.

Label should include the following 3 pieces of information:
Velvet Hearth Studio (company name)
Coconut Lime (this will change depending on fragrance)
Soy Candle

Velvet Hearth Studio does not have a company logo... what is done for the label will set tone for what is done across other elements of business moving forward.

Industry/Entity Type

Business

Requirements
Must have
• Velvet Hearth Studio
Fragrance Flavour
Soy Candle

```html
<!DOCTYPE html>
<html lang="en">
<head>
<meta charset="utf-8">
<title>Velvet Hearth Studio – Lid Label</title>
<link rel="stylesheet" href="https://fonts.googleapis.com/css2?family=Kalam:wght@700&family=Cutive&family=Sacramento&display=swap">
<style>
  :root {
    --page: #ffffff;
    --label-cream: #f9f9eb;
    --label-rim: #000000;
    --ink-black: #0d0d0d;
    --ink-brown: #4a2a14;
    --ink-tan: #8a5a2b;
    --floral-light: #d8d8c6;
    --floral-dark: #5a5a50;
  }
  html, body {
    margin: 0;
    padding: 0;
    width: 1200px;
    height: 1081px;
    overflow: hidden;
    background: var(--page);
  }
  .canvas {
    display: block;
    width: 1200px;
    height: 1081px;
  }
  .label-face { fill: var(--label-cream); }
  .label-rim { fill: none; stroke: var(--label-rim); stroke-width: 4; }
  .brand-name {
    font-family: "Kalam", cursive;
    font-weight: 700;
    font-size: 58px;
    fill: var(--ink-black);
    letter-spacing: 1px;
  }
  .fragrance-name {
    font-family: "Cutive", serif;
    font-size: 38px;
    fill: var(--ink-brown);
  }
  .product-type {
    font-family: "Sacramento", cursive;
    font-size: 54px;
    fill: var(--ink-tan);
  }
</style>
</head>
<body>
<svg class="canvas" viewBox="0 0 1200 1081" xmlns="http://www.w3.org/2000/svg">
  <defs>
    <clipPath id="label-shape">
      <circle cx="331" cy="330" r="328"/>
    </clipPath>
    <linearGradient id="floral-tone" x1="0" y1="0" x2="0" y2="1">
      <stop offset="0" stop-color="var(--floral-light)"/>
      <stop offset="1" stop-color="var(--floral-dark)"/>
    </linearGradient>
  </defs>

  <g class="lid-label">
    <circle class="label-face" cx="331" cy="330" r="328"/>

    <g clip-path="url(#label-shape)">
      <path class="floral-flourish" role="img"
            aria-label="Vintage black line-art floral flourish with roses, leaves and swirling vines across the lower part of the label"
            fill="url(#floral-tone)"
            d="M0,420 C90,360 150,420 230,430 C330,440 400,440 470,420 C520,405 515,330 560,320 L700,320 L700,700 L0,700 Z"/>
    </g>

    <circle class="label-rim" cx="331" cy="330" r="328"/>

    <text class="brand-name" x="331" y="161" text-anchor="middle">Velvet Hearth</text>
    <text class="brand-name" x="331" y="250" text-anchor="middle">Studio</text>

    <text class="fragrance-name" x="331" y="344" text-anchor="middle">Coconut Lime</text>
    <text class="product-type" x="340" y="389" text-anchor="middle">Soy Candle</text>
  </g>
</svg>
</body>
</html>
```